Tech business card design

We need an amazing business card design for our new business 'Brakka' a marketing tech startup based in Sydney, Australia. We provide an online marketplace for businesses to search and buy advertising media, connect with service providers and learn more about marketing. We wish to communicate 'cool tech', reliability and professionalism and design based around our logo.

Target Market(s)

Business Owners

Contact Information for Business Card

Name
Position
Email Address
Website
Phone Number

Font styles to use
Other font styles liked:
• Avenir & Avenir Next

Colors

Designer to choose colors to be used in the design.

```html
<!DOCTYPE html>
<html lang="en">
<head>
<meta charset="utf-8">
<title>Brakka Business Card</title>
<link rel="stylesheet" href="https://fonts.googleapis.com/css2?family=Lato:wght@400;700;900&display=swap">
<style>
  :root {
    --backdrop: #1c1c1f;
    --card-navy: #100f3d;
    --ink-white: #ffffff;
    --ink-soft: #e4e4ee;
    --rule: #6f6f9a;
  }
  * { box-sizing: border-box; margin: 0; padding: 0; }
  html, body {
    width: 1200px; height: 900px; overflow: hidden;
    background: var(--backdrop);
    font-family: "Lato", sans-serif;
  }
  .stage {
    position: relative; width: 1200px; height: 900px;
  }
  .card {
    position: absolute; left: 320px;
    width: 560px; height: 320px;
    background: var(--card-navy);
    border-radius: 22px;
    color: var(--ink-white);
    box-shadow: 0 12px 30px rgba(0,0,0,0.55);
  }
  .card--front { top: 100px; }
  .card--back  { top: 480px; }

  .wordmark {
    font-weight: 900;
    letter-spacing: 1px;
    color: var(--ink-white);
    line-height: 1;
    position: absolute;
  }
  .card--front .wordmark {
    font-size: 96px; left: 50%; top: 50%;
    transform: translate(-50%, -55%);
    color: var(--ink-soft);
  }
  .card--back .wordmark {
    font-size: 84px; right: 40px; top: 56px;
  }

  .divider {
    position: absolute; left: 232px; right: 40px; top: 186px;
    height: 1px; background: var(--rule);
  }
  .website {
    position: absolute; right: 40px; top: 198px;
    font-size: 15px; letter-spacing: 0.3px;
  }
  .contact {
    position: absolute; left: 36px; top: 170px;
  }
  .contact__name {
    font-weight: 900; font-size: 21px; letter-spacing: 0.5px;
  }
  .contact__role {
    font-size: 15px; margin-top: 2px; color: var(--ink-soft);
  }
  .contact__list {
    list-style: none; margin-top: 16px; font-size: 16px;
  }
  .contact__item {
    display: flex; align-items: center; gap: 8px; margin-top: 4px;
  }
  .contact__icon { width: 16px; height: 16px; fill: var(--ink-white); }
</style>
</head>
<body>
<main class="stage">
  <section class="card card--front">
    <span class="wordmark">brakka</span>
  </section>

  <section class="card card--back">
    <span class="wordmark">brakka</span>
    <div class="divider"></div>
    <p class="website">www.brakka.com</p>
    <div class="contact">
      <p class="contact__name">DANIEL MOORE</p>
      <p class="contact__role">Managing Director</p>
      <ul class="contact__list">
        <li class="contact__item">
          <svg class="contact__icon" viewBox="0 0 16 16" aria-hidden="true">
            <path d="M2 5c0-2 2-3 6-3s6 1 6 3v1h-3V5H5v1H2z"/>
            <rect x="3" y="7" width="10" height="7" rx="1.5"/>
          </svg>
          <span>044-987 654 321</span>
        </li>
        <li class="contact__item">
          <svg class="contact__icon" viewBox="0 0 16 16" aria-hidden="true">
            <path d="M1 3h14v10H1z M2 4l6 5 6-5" fill="var(--ink-white)" stroke="var(--card-navy)" stroke-width="1"/>
          </svg>
          <span>hello@brakka.com</span>
        </li>
      </ul>
    </div>
  </section>
</main>
</body>
</html>
```